I am an accountant and I am interested in publicising workshops, seminars and networking events. I have included some publicity materials produced by my franchise company which can be used as a basis for the design.

Side 1: should show the basic design. I need my contact details to be included as follows: Jenna Pricott, Lumbrell Accounting, 47 Harcombe Street, Fennwick Row, EC1V 8QN. Tel: 07412 637208. Email: jennapricott@lumbrell.example
www.lumbrellnorthside.example

Side 2: can use elements of the basic design submitted or parts of the franchise website for www.lumbrell.example. This side should lead people to my workshops. These are detailed here on this website www.lumbrell.example. (seminars top menu) At the moment there are four seminars, so they should not go into detail about any specific seminar as they may change in the future. I also have a free ebook so I also want this mentioned in the text.

```html
<!DOCTYPE html>
<html lang="en">
<head>
<meta charset="utf-8">
<title>Lumbrell Accounting – Seminars Flyer</title>
<link href="https://fonts.googleapis.com/css2?family=Sorts+Mill+Goudy:ital@0;1&display=swap" rel="stylesheet">
<style>
  :root {
    --page-bg: #e8e8e8;
    --paper: #ffffff;
    --band-start: #f0ad32;
    --band-end: #f7c970;
    --accent: #e9a93a;
    --ink: #3b3b3b;
    --body-ink: #4a4a4a;
    --brand-navy: #1f3f8f;
    --frame: #f0c27a;
  }
  * { box-sizing: border-box; margin: 0; padding: 0; }
  html, body {
    width: 1040px; height: 1200px; overflow: hidden;
    background: var(--page-bg);
    font-family: "Sorts Mill Goudy", Georgia, serif;
  }
  .flyer {
    position: absolute; top: 278px;
    width: 880px; height: 1134px;
    background: var(--paper);
    box-shadow: 0 6px 24px rgba(0,0,0,0.18);
    transform: scale(0.5682);
    transform-origin: top left;
    overflow: hidden;
  }
  .flyer--front { left: 13px; }
  .flyer--back { left: 527px; }

  /* ---------- Front ---------- */
  .flyer__band {
    position: absolute; left: 0; top: 0; width: 100%; height: 60px;
    background: linear-gradient(90deg, var(--band-start), var(--band-end) 70%, var(--band-start));
  }
  .flyer__main {
    position: absolute; left: 0; top: 60px; width: 530px; height: 1074px;
  }
  .headline {
    position: absolute; left: 0; top: 50px; width: 530px;
    text-align: center; color: var(--ink);
    font-size: 52px; line-height: 64px; font-weight: 400;
  }
  .profile__photo {
    position: absolute; left: 45px; top: 226px; width: 153px; height: 201px;
    border: 2px solid #c8c8c8;
    background: linear-gradient(160deg, #f2f2f2, #9a9a9a 60%, #5e5e5e);
  }
  .profile__text {
    position: absolute; left: 227px; top: 226px; width: 285px;
    color: var(--body-ink); font-size: 15.5px; line-height: 27.3px;
  }
  .profile__name { color: var(--accent); font-size: 21px; }
  .profile__cred { font-style: italic; color: var(--ink); font-size: 15px; }
  .events {
    position: absolute; left: 0; top: 638px; width: 530px;
    text-align: center; color: var(--accent); font-size: 25px;
  }
  .visit {
    position: absolute; left: 40px; top: 686px; width: 450px;
    text-align: center; color: var(--accent); font-size: 25px; line-height: 34px;
  }
  .ebook {
    position: absolute; left: 0; top: 796px; width: 530px;
    text-align: center; color: var(--ink); font-size: 31px; letter-spacing: 0.5px;
  }
  .brand {
    display: flex; align-items: center; gap: 14px;
  }
  .brand--stacked {
    position: absolute; left: 0; top: 850px; width: 530px;
    flex-direction: column; gap: 12px;
  }
  .brand__dot {
    width: 40px; height: 40px; border-radius: 50%;
    background: var(--accent);
  }
  .brand__name {
    color: var(--brand-navy); font-size: 44px; line-height: 1;
  }
  .contact {
    color: var(--body-ink); font-size: 15px; line-height: 22px;
  }
  .contact--front {
    position: absolute; left: 0; top: 968px; width: 530px; text-align: center;
  }
  .gallery {
    position: absolute; left: 534px; top: 60px; width: 346px;
  }
  .gallery__frame {
    position: absolute; left: 0; width: 346px;
    border: 2px solid var(--frame);
  }
  .gallery__frame--team { top: 0; height: 322px;
    background: radial-gradient(ellipse at 55% 50%, #ffffff 30%, #d8d8d8 55%, #e6a548 75%, #ffffff 92%); }
  .gallery__frame--bowl { top: 348px; height: 320px;
    background: radial-gradient(circle at 50% 55%, #ffffff 25%, #e2e6ea 55%, #c9ced3 68%, #ffffff 80%); }
  .gallery__frame--chart { top: 694px; height: 324px;
    background: linear-gradient(160deg, #e4e4e4, #b9b9b9 45%, #8e8e8e 70%, #e9b26a 90%); }

  /* ---------- Back ---------- */
  .back__band {
    position: absolute; left: 0; top: 60px; width: 100%; height: 200px;
    background: linear-gradient(90deg, var(--band-start), var(--band-end) 70%, var(--band-start));
    display: flex; align-items: center; padding: 0 50px;
  }
  .back__headline {
    color: #ffffff; font-size: 50px; line-height: 62px; font-weight: 400;
  }
  .back__coins {
    position: absolute; left: 45px; top: 300px; width: 170px; height: 580px;
    background: linear-gradient(90deg, #8a6a2e, #d9b46a 35%, #f3dca0 50%, #c9a050 70%, #7a5a22);
  }
  .back__copy {
    position: absolute; left: 250px; top: 300px; width: 590px;
    display: flex; flex-direction: column; gap: 22px;
    color: var(--body-ink); font-size: 18px; line-height: 29px;
  }
  .back__heading {
    color: var(--ink); font-size: 28px; line-height: 34px; font-weight: 400;
  }
  .back__cta {
    color: var(--accent); font-size: 23px; line-height: 32px;
  }
  .contact--back { font-size: 17px; line-height: 26px; }
  .brand--back {
    position: absolute; right: 40px; top: 1030px;
  }
</style>
</head>
<body>
  <!-- Side 1 -->
  <article class="flyer flyer--front">
    <div class="flyer__band"></div>

    <section class="flyer__main">
      <h1 class="headline">We Take Pride in<br>Helping our Clients</h1>

      <div class="profile__photo" role="img" aria-label="Portrait photo of Jenna Pricott"></div>
      <p class="profile__text">
        <span class="profile__name">Jenna Pricott</span> <span class="profile__cred">– BSc MAAT</span><br>
        Jenna is a qualified accountant with extensive experience in industry. She is fully conversant with accounting and tax issues relating to Start-ups, Entre­preneurs and Small to Medium Sized Companies. She has over 8 years experience in tax, book keeping and management accounts of various companies with multi-million turnover. Jenna has an iron-clad reputation, with a focus on your financial success. She gets results and looks at every situation with fresh eyes.
      </p>

      <p class="events">Join our networking events and seminars</p>
      <p class="visit">Visit www.lumbrellnorthside.example for more information and to arrange your booking today.</p>
      <p class="ebook">Free ebook available!</p>

      <div class="brand brand--stacked">
        <span class="brand__dot"></span>
        <span class="brand__name">Lumbrell Accounting</span>
      </div>

      <address class="contact contact--front" style="font-style: normal;">
        Jenna Pricott, Lumbrell Accounting<br>
        47 Harcombe Street, Fennwick Row, EC1V 8QN<br>
        Tel: 07412 637208 · Email: jennapricott@lumbrell.example
      </address>
    </section>

    <aside class="gallery">
      <div class="gallery__frame gallery__frame--team" role="img" aria-label="Ring of small figures holding hands, silver and orange"></div>
      <div class="gallery__frame gallery__frame--bowl" role="img" aria-label="Two goldfish facing each other in a glass bowl"></div>
      <div class="gallery__frame gallery__frame--chart" role="img" aria-label="Silver 3D pie chart with one orange slice pulled out"></div>
    </aside>
  </article>

  <!-- Side 2 -->
  <article class="flyer flyer--back">
    <div class="flyer__band"></div>
    <div class="back__band">
      <h2 class="back__headline">A good accountant is worth their weight in gold</h2>
    </div>

    <div class="back__coins" role="img" aria-label="Tall stack of gold coins"></div>

    <div class="back__copy">
      <p>Our seminars and workshops give business owners practical guidance on the financial topics that matter most, in a relaxed and friendly setting.</p>
      <h3 class="back__heading">Seminars, workshops and networking events</h3>
      <p>We run a regular programme of sessions for start-ups, entrepreneurs and growing companies. Meet like-minded business owners, ask questions and leave with clear next steps.</p>
      <h3 class="back__heading">Free ebook available!</h3>
      <p>Request your free ebook and find out how to keep more of what you earn.</p>
      <p class="back__cta">See our current seminars and book your place at www.lumbrell.example</p>
      <address class="contact contact--back" style="font-style: normal;">
        Jenna Pricott, Lumbrell Accounting<br>
        47 Harcombe Street, Fennwick Row, EC1V 8QN<br>
        Tel: 07412 637208<br>
        Email: jennapricott@lumbrell.example<br>
        www.lumbrellnorthside.example
      </address>
    </div>

    <div class="brand brand--back">
      <span class="brand__dot"></span>
      <span class="brand__name">Lumbrell Accounting</span>
    </div>
  </article>
</body>
</html>
```